Banner Ad for Resume Services Website

The add is for this web site: www.BrightFolioDesk.com

The site offers 4 different services:

- Resume Writing (by a Certified Professional Resume Writer)
- Resume Posting (posts your resume to 85 job sites)
- Resume Distribution (sends your resume to hundreds of recruiters)
- Resume Online website (created an online resume with a domain name to your name)

Colors to be used are Blue, Yellow, etc... please check the website for inspiration.

Check the web site to learn more.

Target Market(s)

Unemployed, Professionals who want to switch jobs, etc..

Industry/Entity Type

Learn

Requirements
Must have
• We definitely one this to be included on the banner:

"Free Resume Samples"

in order to attract clicks.
Nice to have
• Some of the words we suggest to include on the banner are:

"How Good is Your Resume? Ask a Professional !"

Should not have
• No animation !

Do not place the LOGO on the banner as our LOGO might change in the near future. If you already submitted a banner with the LOGO on it, you can replace it with any other graphic that has a Resume/Jobs/BusinessStaff related theme.

```html
<!DOCTYPE html>
<html lang="en">
<head>
<meta charset="utf-8">
<title>Free Resume Samples – BrightFolioDesk</title>
<link rel="stylesheet" href="https://fonts.googleapis.com/css2?family=Arimo:wght@400;700&family=Noto+Sans:wght@400;700&display=swap">
<style>
  :root {
    --page-bg: #ffffff;
    --body-text: #555555;
    --edge-shade: #e4e4e4;
    --banner-blue-top: #1b9be0;
    --banner-blue-bottom: #0a6cbc;
    --photo-light: #e9ecef;
    --photo-mid: #b7c0c8;
    --caption-bg: #ececec;
    --caption-text: #444444;
    --note-yellow: #f6ef6a;
    --box-bg: #eeeeee;
    --box-border: #cfcfcf;
    --box-inner: #ffffff;
    --heading-text: #222222;
    --icon-blue: #1f6fd1;
    --footer-top: #0c5aa6;
    --footer-bottom: #0a4c8e;
    --footer-muted: #7f95b0;
    --footer-link: #ffffff;
  }
  * { margin: 0; padding: 0; box-sizing: border-box; }
  html, body { width: 1200px; height: 900px; overflow: hidden; background: var(--page-bg); }
  .page { position: relative; width: 1200px; height: 900px; overflow: hidden; font-family: "Noto Sans", Verdana, sans-serif; }
  .page-edge { position: absolute; left: 0; top: 0; width: 18px; height: 801px;
    background: linear-gradient(to right, #f6f6f6, var(--edge-shade) 80%, #d6d6d6); }

  .intro { position: absolute; left: 45px; top: 0; width: 740px; color: var(--body-text);
    font-size: 16px; line-height: 27.4px; text-align: justify; }
  .intro span { display: block; white-space: nowrap; text-align-last: justify; }
  .intro span.last { text-align-last: left; }

  .banner { position: absolute; left: 43px; top: 280px; width: 1093px; height: 135px; display: flex; }
  .banner-photo { width: 321px; height: 135px; position: relative; }
  .banner-photo .scene { height: 113px;
    background: linear-gradient(180deg, var(--photo-light) 0%, #d3d9de 55%, var(--photo-mid) 100%); }
  .banner-photo .caption { height: 22px; background: var(--caption-bg); color: var(--caption-text);
    font-family: "Arimo", Arial, sans-serif; font-weight: 700; font-size: 17px; line-height: 22px; padding-left: 12px; }
  .banner-message { flex: 1; position: relative;
    background: linear-gradient(180deg, var(--banner-blue-top), var(--banner-blue-bottom)); color: #fff;
    font-family: "Arimo", Arial, sans-serif; }
  .banner-title { position: absolute; left: 21px; top: 8px; font-size: 49px; font-weight: 700; letter-spacing: -0.3px; }
  .banner-subtitle { position: absolute; left: 21px; top: 67px; font-size: 22px; font-weight: 700; }
  .banner-note { position: absolute; right: 12px; top: 2px; width: 186px; height: 130px;
    background: var(--note-yellow); transform: rotate(-2deg); }

  .promo-box { position: absolute; left: 45px; width: 809px; background: var(--box-bg); border: 1.5px solid var(--box-border); }
  .promo-box h2 { font-size: 19px; font-weight: 700; color: var(--heading-text); margin: 2px 0 0 30px; line-height: 24px; }
  .promo-body { position: absolute; left: 15px; right: 15px; background: var(--box-inner); display: flex; align-items: center; }
  .promo-body p { font-size: 18px; font-weight: 700; color: var(--heading-text); }

  .promo-app { top: 455px; height: 144px; }
  .promo-app .promo-body { top: 29px; height: 97px; }
  .promo-app svg { margin-left: 27px; margin-right: 22px; }
  .promo-cert { top: 642px; height: 129px; }
  .promo-cert .promo-body { top: 29px; height: 83px; }
  .promo-cert svg { margin-left: 36px; margin-right: 26px; }

  .site-footer { position: absolute; left: 0; top: 801px; width: 1200px; height: 99px;
    background: linear-gradient(180deg, var(--footer-top), var(--footer-bottom)); font-size: 17px; }
  .copyright { position: absolute; top: 5px; left: 443px; color: var(--footer-muted); white-space: nowrap; }
  .copyright a { color: var(--footer-link); text-decoration: none; }
  .footer-nav { position: absolute; top: 33px; left: 4px; color: var(--footer-link); white-space: nowrap; font-size: 17.3px; }
  .footer-nav a { color: var(--footer-link); text-decoration: none; }
</style>
</head>
<body>
<div class="page">
  <div class="page-edge"></div>

  <div class="intro">
    <span>hiring new staff. Vacancies are frequently created when a company has issues or an increase</span>
    <span>in business. Your resume and your approach have to reassure management that you can</span>
    <span>solve their issues if they hire YOU. With the competition being as tough as it is now, there is</span>
    <span>no room for mistakes or weaknesses in highlighting your qualifications and experience to</span>
    <span>potential employers. Getting hired with the aid of technology and the Internet is a time-saving</span>
    <span>proposition for all serious candidates. Today, the Internet is your biggest ally for getting</span>
    <span>exposure. Putting a clean and attractive resume online will expose you to a whole range of</span>
    <span>new people that you might not have know were looking for your qualifications. Let us show</span>
    <span class="last">you how to improve your appearance and maximize your exposure...</span>
  </div>

  <div class="banner">
    <div class="banner-photo">
      <div class="scene" role="img" aria-label="Business team of professionals standing on an office balcony"></div>
      <div class="caption">brightfoliodesk.com</div>
    </div>
    <div class="banner-message">
      <div class="banner-title">Free Resume Samples</div>
      <div class="banner-subtitle">How Good is Your Resume? Ask a Professional!</div>
      <div class="banner-note" role="img" aria-label="Yellow sticky note pinned with a handwritten Good Job message"></div>
    </div>
  </div>

  <section class="promo-box promo-app">
    <h2>Check our PocketPhone/SlateTab app in AppMarket</h2>
    <div class="promo-body">
      <svg width="38" height="63" viewBox="0 0 38 63" aria-hidden="true">
        <rect x="1" y="1" width="36" height="61" rx="6" fill="#1a1a1a"/>
        <rect x="4" y="9" width="30" height="43" fill="#4a4f55"/>
        <circle cx="19" cy="57" r="2.6" fill="#555"/>
        <rect x="15" y="4" width="8" height="1.6" rx="0.8" fill="#555"/>
      </svg>
      <p>Tips and Videos on Resume Writing, Cover letters and Job Search</p>
    </div>
  </section>

  <section class="promo-box promo-cert">
    <h2>Become a Certified Project Manager</h2>
    <div class="promo-body">
      <svg width="48" height="46" viewBox="0 0 48 46" role="img" aria-label="Blue puzzle piece icon">
        <rect x="6" y="8" width="34" height="34" rx="3" fill="var(--icon-blue)"/>
      </svg>
      <p>PCM Certification Exam Training: Increase your chances of success</p>
    </div>
  </section>

  <footer class="site-footer">
    <div class="copyright">Copyright © 2011 <a href="#">BrightFolioDesk.com</a>. All Rights Reserved.</div>
    <nav class="footer-nav">
      <a href="#">Home</a> | <a href="#">Why Online Resumes</a> | <a href="#">Sample Resumes</a> | <a href="#">Form</a> | <a href="#">Resume Writing</a> | <a href="#">Resume Posting</a> | <a href="#">Resume Distribution</a> | <a href="#">Tips &amp; Tricks</a> | <a href="#">Links</a> | <a href="#">Site Map</a>
    </nav>
  </footer>
</div>
</body>
</html>
```